Professional website for psychological services

Create a professional, easy to navigate website using soothing coastal images and incorporate company logo in design. Website is for a small private clinic that provides psychological services and must be appealing to professional men and women. A website I really like is www.velmorlodge.example I would love something like similar.

Target Market(s)

Professional men and women seeking psychological services

Industry/Entity Type

Mental Health

Number of Pages Required

5+ page

Requirements
Must have
• The website must incorporate the logo provided. The name of the company/website is Brindle Oak Wellness Aftercare. Colors must compliment the logo, must be coastal and soothing yet very professional. I would like a website like www.velmorlodge.example
• Pages will be:Home, Services, FAQ and Contact Us. The images included of the building and office are for the contact us page. Under the tab Servies: Individual Psychotherapy, Family Therapy, EMDR I will provide specific content for each.
Nice to have
• I want the website to be easy to navigate and the font easy to read. The writing on the logo is very light and I'm open to changing it slightly if it will be better aesthetically.
Should not have
• Please no pictures of any swimsuits, alcoholic beverages, etc. This is a professional psychological clinic.

```html
<!DOCTYPE html>
<html lang="en">
<head>
<meta charset="utf-8">
<title>Brindle Oak Wellness Aftercare</title>
<link href="https://fonts.googleapis.com/css2?family=Lato:wght@400;700;900&family=Parisienne&family=Oswald:wght@300;400&display=swap" rel="stylesheet">
<style>
:root{
  --teal:#25b4d3;
  --teal-dark:#1b8fab;
  --brown:#a57b4b;
  --tan:#d8b58c;
  --beige:#efe9e0;
  --ink:#333a3f;
  --muted:#6d7479;
  --line:#dfe3e6;
  --footer:#eef2f3;
  --band:#6a5848;
  --bar:#5b4a3c;
  --white:#ffffff;
}
*{box-sizing:border-box;margin:0;padding:0}
html,body{width:1200px;height:3371px;overflow:hidden}
body{position:relative;background:var(--white);font-family:'Lato',sans-serif;color:var(--ink);font-size:13px;line-height:1.55}
.abs{position:absolute}
.script{font-family:'Parisienne',cursive;font-weight:400}
.teal{color:var(--teal)}

/* header */
.site-header{position:absolute;left:0;top:0;width:1200px;height:158px;background:var(--white)}
.social{position:absolute;top:48px;display:flex;gap:10px}
.social span{width:26px;height:26px;border-radius:50%;border:1px solid var(--teal);display:block}
.brand{position:absolute;left:0;width:1200px;top:26px;text-align:center;color:var(--teal);font-weight:400;letter-spacing:1px}
.brand .dot{display:block;width:18px;height:18px;border-radius:50%;background:var(--teal);margin:0 auto 6px}
.brand .name{font-size:20px;line-height:1.1}
.brand .sub{font-size:9px;letter-spacing:4px;text-transform:uppercase;line-height:1.6}
.phone-pill{position:absolute;left:849px;top:48px;width:140px;height:32px;border:1px solid var(--line);border-radius:16px;display:flex;align-items:center;justify-content:center;gap:6px;font-size:12px;color:var(--ink)}
.header-rule{position:absolute;left:213px;top:110px;width:776px;height:1px;background:var(--line)}
.main-nav{position:absolute;left:0;top:124px;width:1200px;display:flex;justify-content:center;gap:30px;font-size:11px;text-transform:uppercase;letter-spacing:.5px}
.main-nav a{color:var(--ink);text-decoration:none;padding-bottom:6px}
.main-nav a.active{color:var(--teal);border-bottom:2px solid var(--teal)}

/* hero */
.hero{position:absolute;left:0;top:158px;width:1200px;height:505px;background:linear-gradient(100deg,#6f8f4e 0%,#9cb07a 18%,#c9d3c6 34%,#8fb9cf 52%,#3e8fb8 72%,#1f6f99 100%)}
.start-form{position:absolute;left:190px;top:65px;width:340px;height:340px;border-radius:50%;background:rgba(240,247,250,.95);border:10px solid var(--teal);box-shadow:0 0 0 4px rgba(255,255,255,.8)}
.start-form h2{position:absolute;top:38px;width:100%;text-align:center;font-size:30px;color:var(--teal)}
.field{position:absolute;background:var(--white);border:1px solid var(--line);font-size:9px;color:#888;padding:0 8px;display:flex;align-items:center}
.start-form .field{left:43px;width:247px;height:30px}
.btn{position:absolute;display:flex;align-items:center;justify-content:center;gap:6px;color:var(--white);font-size:10px;font-weight:700;letter-spacing:.5px;text-transform:uppercase;border-radius:16px}
.btn-tan{background:var(--tan)}
.btn-teal{background:var(--teal);box-shadow:0 3px 8px rgba(37,180,211,.35)}
.hero-copy{position:absolute;left:629px;top:180px;color:var(--white)}
.hero-copy .kicker{font-size:36px;line-height:1}
.hero-copy .title{font-family:'Oswald',sans-serif;font-weight:300;font-size:36px;letter-spacing:2px;line-height:1.3}
.hero-copy .sub{font-size:10px;font-weight:700;letter-spacing:.3px}

/* shared section parts */
.section{position:absolute;left:0;width:1200px}
.beige-panel{position:absolute;top:0;height:100%;background:linear-gradient(135deg,#f1ece4,#e6ddd0)}
.mark{position:absolute;width:20px;height:20px;border-radius:50%;border:2px solid var(--teal)}
.heading{position:absolute;font-size:46px;color:var(--teal);line-height:1}
.heading-rule{position:absolute;width:40px;height:2px;background:var(--line)}
.photo-ring{position:absolute;border-radius:50%;border:12px solid var(--teal);box-shadow:0 0 0 4px var(--white)}
.photo-ring .photo{width:100%;height:100%;border-radius:50%}
.lead{position:absolute;font-weight:700;font-size:12.5px;line-height:1.6}
.body-text{position:absolute;font-size:11.5px;color:var(--muted);line-height:1.6}
.item{position:absolute;display:flex;gap:14px;width:400px}
.item .icon{flex:0 0 54px;height:54px;border-radius:50%;background:var(--brown);border:3px solid #e7d6c0;display:flex;align-items:center;justify-content:center}
.item h3{font-size:11.5px;font-weight:400;text-transform:uppercase;color:var(--ink)}
.item h3 b{color:var(--teal);font-weight:400}
.item p{font-size:11px;color:var(--muted);line-height:1.55}
.item p i{color:var(--teal);font-style:normal}

/* testimonials */
.testimonials{background:linear-gradient(180deg,#27b5d4 0%,#1ea6c7 60%,#2b8fae 100%)}
.t-title{position:absolute;top:70px;width:100%;text-align:center;font-size:42px;color:var(--white)}
.t-card{position:absolute;top:160px;width:330px;height:79px;padding:10px 14px 0 44px;font-size:10.5px;font-style:italic;line-height:1.5;color:var(--white)}
.t-card.light{left:252px;background:rgba(255,255,255,.55);color:#f4fbfd}
.t-card.dark{left:618px;background:rgba(12,80,100,.55)}
.t-card .q{position:absolute;left:12px;top:4px;font-size:34px;font-style:normal;line-height:1;opacity:.7}
.t-person{position:absolute;top:255px;display:flex;align-items:center;gap:8px;color:var(--white)}
.t-person .avatar{width:42px;height:42px;border-radius:50%;border:2px solid var(--white);background:linear-gradient(135deg,#c9b6a6,#7f6a5c)}
.t-person b{display:block;font-size:10.5px;text-transform:uppercase}
.t-person .stars{font-size:10px;letter-spacing:2px}
.arrow{position:absolute;top:196px;width:30px;height:30px;border-radius:50%;border:1px solid rgba(255,255,255,.7);display:flex;align-items:center;justify-content:center}

/* appointment */
.appointment{background:linear-gradient(180deg,#d9e2e8 0%,#eef0ef 45%,#c7d5dc 75%,#a9b8bf 100%)}
.appointment .field{height:36px}

/* mailing */
.mailing{background:linear-gradient(90deg,#6b5747,#7b6656,#5f4f42)}
.mailing h2{position:absolute;left:209px;top:34px;font-size:22px;font-weight:700;color:var(--white)}

/* footer */
.site-footer{background:var(--footer)}
.f-col{position:absolute;top:83px}
.f-col h4{font-size:16px;font-weight:700;color:var(--teal);margin-bottom:6px}
.f-col .rule{width:40px;height:2px;background:var(--line);margin-bottom:16px}
.f-col ul{list-style:none;font-size:11.5px;line-height:2}
.f-col li::before{content:"›";color:var(--teal);margin-right:8px}
.f-brand{color:var(--teal);font-size:15px;text-align:center;width:110px;line-height:1.2;margin-bottom:18px}
.f-brand .dot{display:block;width:14px;height:14px;border-radius:50%;background:var(--teal);margin:0 auto 6px}
.f-brand small{display:block;font-size:7px;letter-spacing:2px;text-transform:uppercase}
.f-social{display:flex;gap:8px;margin-left:12px}
.f-social span{width:20px;height:20px;border-radius:50%;border:1px solid var(--teal)}
.contact-row{display:flex;gap:10px;margin-bottom:12px;font-size:11px;line-height:1.5}
.contact-row b{color:var(--ink);display:block;font-size:11.5px}
.copyright{position:absolute;left:0;top:3332px;width:1200px;height:39px;background:var(--bar);color:#e8dccf;font-size:10px;display:flex;align-items:center;justify-content:center;letter-spacing:.3px}
</style>
</head>
<body>

<header class="site-header">
  <div class="social" style="left:213px" aria-label="Social links"><span></span><span></span><span></span><span></span></div>
  <div class="brand"><span class="dot"></span><div class="name">Brindle Oak</div><div class="sub">Wellness Aftercare</div></div>
  <div class="phone-pill">
    <svg width="12" height="12" viewBox="0 0 24 24"><path fill="#25b4d3" d="M6.6 10.8a15 15 0 0 0 6.6 6.6l2.2-2.2c.3-.3.7-.4 1-.2 1.1.4 2.3.6 3.6.6.6 0 1 .4 1 1V20c0 .6-.4 1-1 1A17 17 0 0 1 3 4c0-.6.4-1 1-1h3.5c.6 0 1 .4 1 1 0 1.3.2 2.5.6 3.6.1.3 0 .7-.2 1z"/></svg>
    555-014-2290
  </div>
  <div class="header-rule"></div>
  <nav class="main-nav">
    <a class="active" href="#">Home</a><a href="#">About Us</a><a href="#">Services</a><a href="#">Press</a><a href="#">FAQ</a><a href="#">Testimonials</a><a href="#">Contact Us</a>
  </nav>
</header>

<section class="hero" role="img" aria-label="Coastal cliffs with green grass above a curving beach and blue sea">
  <form class="start-form">
    <h2 class="script">Getting Started</h2>
    <div class="field" style="top:78px">Name</div>
    <div class="field" style="top:114px">Phone</div>
    <div class="field" style="top:150px">Email</div>
    <div class="field" style="top:174px;height:60px;align-items:flex-start;padding-top:6px">Message</div>
    <div class="btn btn-tan" style="left:103px;top:245px;width:120px;height:32px">Submit Now</div>
  </form>
  <div class="hero-copy">
    <div class="kicker script">Intensive &amp; Comprehensive</div>
    <div class="title">MENTAL HEALTH SERVICES</div>
    <div class="sub">TO WOMEN &amp; MEN SUFFERING FROM SUBSTANCE ABUSE AND ADDICTION</div>
  </div>
</section>

<section class="section about" style="top:663px;height:487px">
  <div class="beige-panel" style="left:787px;width:413px" role="img" aria-label="Faded portrait backdrop in warm beige tones"></div>
  <span class="mark" style="left:215px;top:50px"></span>
  <h2 class="heading script" style="left:209px;top:80px">Who we are</h2>
  <div class="heading-rule" style="left:209px;top:134px"></div>
  <p class="lead" style="left:209px;top:162px;width:443px">Hi! I am Marion T. Hale Registered Psychologist and Canadian Certified Counsellor.</p>
  <p class="body-text" style="left:209px;top:209px;width:443px">We are offering intensive and comprehensive mental health services to men and women recovering from addiction and mental illness.</p>
  <blockquote class="body-text" style="left:209px;top:269px;width:391px;height:102px;border:1px solid var(--line);padding:14px 14px 0 46px;font-style:italic">
    <span class="abs" style="left:12px;top:4px;font-size:36px;color:#cfd4d7;font-style:normal">&ldquo;</span>
    Lorem ipsum dolor sit amet, consectetur adipiscing elit. Nullam lacinia posuere felis vel ultricies. Integer elit elit, aliquet in condimentum et, ultrices sed nibh. Pellentesque vel est dui. Curabitur et neque ultrices diam facilisis iaculis at non urna.
  </blockquote>
  <p class="abs teal" style="left:209px;top:388px;font-size:11.5px">Marion T. Hale</p>
  <div class="photo-ring" style="left:674px;top:101px;width:270px;height:270px">
    <div class="photo" role="img" aria-label="Portrait of the clinic's psychologist" style="background:radial-gradient(circle at 50% 40%,#d9c2ae,#6b4a3a 70%,#e9e6e2)"></div>
  </div>
</section>

<section class="section services" style="top:1150px;height:486px;background:#faf8f5">
  <div class="beige-panel" style="left:0;width:434px" role="img" aria-label="Faded counselling session backdrop in beige tones"></div>
  <div class="photo-ring" style="left:236px;top:86px;width:314px;height:314px">
    <div class="photo" role="img" aria-label="Video still of a distressed man in a therapy session" style="background:linear-gradient(135deg,#b7866a,#d8cdc2 50%,#8fb5cf)"></div>
  </div>
  <svg class="abs" style="left:368px;top:218px" width="50" height="50" viewBox="0 0 50 50" aria-hidden="true"><circle cx="25" cy="25" r="24" fill="#25b4d3"/><path d="M20 15l14 10-14 10z" fill="#fff"/></svg>
  <span class="mark" style="left:635px;top:55px"></span>
  <h2 class="heading script" style="left:629px;top:86px">What we do</h2>
  <div class="heading-rule" style="left:629px;top:140px"></div>
  <div class="item" style="left:632px;top:160px"><span class="icon"><svg width="22" height="22" viewBox="0 0 24 24"><circle cx="8" cy="8" r="3" fill="#fff"/><circle cx="16" cy="8" r="3" fill="#fff"/><path d="M2 20c0-4 3-6 6-6s6 2 6 6zM10 20c0-4 3-6 6-6s6 2 6 6z" fill="#fff"/></svg></span><div><h3><b>Individual &amp; Group</b> Psychotherapy</h3><p>Lorem ipsum dolor sit amet, consectetur adipiscing elit. Ut id l mus sit amet justo rhoncus, auctor sapien vitae... <i>[+]</i></p></div></div>
  <div class="item" style="left:632px;top:245px"><span class="icon"><svg width="22" height="22" viewBox="0 0 24 24"><circle cx="7" cy="6" r="2.5" fill="#fff"/><circle cx="17" cy="6" r="2.5" fill="#fff"/><circle cx="12" cy="12" r="2" fill="#fff"/><path d="M4 21v-8h6v8zM14 21v-8h6v8z" fill="#fff"/></svg></span><div><h3><b>Family</b> Therapy</h3><p>Lorem ipsum dolor sit amet, consectetur adipiscing elit. Ut id l mus sit amet justo rhoncus, auctor sapien vitae... <i>[+]</i></p></div></div>
  <div class="item" style="left:632px;top:325px"><span class="icon"><svg width="24" height="24" viewBox="0 0 24 24"><path d="M1 12s4-7 11-7 11 7 11 7-4 7-11 7S1 12 1 12z" fill="#fff"/><circle cx="12" cy="12" r="3.5" fill="#a57b4b"/></svg></span><div><h3><b>EMDR</b> Therapy</h3><p>Lorem ipsum dolor sit amet, consectetur adipiscing elit. Ut id l mus sit amet justo rhoncus, auctor sapien vitae... <i>[+]</i></p></div></div>
  <div class="btn btn-teal" style="left:636px;top:400px;width:120px;height:32px">Learn More <span>&#9656;</span></div>
</section>

<section class="section why" style="top:1636px;height:485px">
  <div class="beige-panel" style="left:787px;width:413px" role="img" aria-label="Faded consultation backdrop in beige tones"></div>
  <span class="mark" style="left:215px;top:50px"></span>
  <h2 class="heading script" style="left:209px;top:82px">Why choose us</h2>
  <div class="heading-rule" style="left:209px;top:136px"></div>
  <div class="item" style="left:207px;top:162px;width:420px"><span class="icon"><svg width="22" height="22" viewBox="0 0 24 24"><circle cx="12" cy="7" r="4" fill="#fff"/><path d="M4 21c0-5 4-8 8-8s8 3 8 8z" fill="#fff"/></svg></span><div><h3><b>Intensive &amp; Comprehensive</b> Mental Health Services</h3><p>Lorem ipsum dolor sit amet, consectetur adipiscing elit. Ut id l mus sit amet justo rhoncus, auctor sapien vitae... <i>[+]</i></p></div></div>
  <div class="item" style="left:207px;top:241px;width:420px"><span class="icon"><svg width="22" height="22" viewBox="0 0 24 24"><circle cx="12" cy="6" r="3.5" fill="#fff"/><path d="M6 21v-7c0-2 2-4 6-4s6 2 6 4v7z" fill="#fff"/></svg></span><div><h3><b>Substance Abuse and</b> Addiction and Mental Illness</h3><p>Lorem ipsum dolor sit amet, consectetur adipiscing elit. Ut id l mus sit amet justo rhoncus, auctor sapien vitae... <i>[+]</i></p></div></div>
  <div class="item" style="left:207px;top:322px;width:420px"><span class="icon"><svg width="22" height="22" viewBox="0 0 24 24"><circle cx="12" cy="9" r="6" fill="#fff"/><path d="M8 14l-2 8 6-3 6 3-2-8z" fill="#fff"/></svg></span><div><h3><b>The Most Trusted Psychotherapy</b> Brindle Oak</h3><p>Lorem ipsum dolor sit amet, consectetur adipiscing elit. Ut id l mus sit amet justo rhoncus, auctor sapien vitae... <i>[+]</i></p></div></div>
  <div class="btn btn-teal" style="left:209px;top:400px;width:121px;height:32px">Learn More <span>&#9656;</span></div>
  <div class="photo-ring" style="left:652px;top:83px;width:314px;height:314px">
    <div class="photo" role="img" aria-label="Smiling woman talking with a counsellor" style="background:linear-gradient(135deg,#e8ecef,#7d9bb8 55%,#3f5e84)"></div>
  </div>
</section>

<section class="section testimonials" style="top:2121px;height:351px" aria-label="Testimonials over a coastal rocks backdrop">
  <h2 class="t-title script">Our Testimonials</h2>
  <div class="arrow" style="left:181px"><svg width="10" height="10" viewBox="0 0 10 10"><path d="M7 1L3 5l4 4" stroke="#fff" stroke-width="1.5" fill="none"/></svg></div>
  <div class="arrow" style="left:987px"><svg width="10" height="10" viewBox="0 0 10 10"><path d="M3 1l4 4-4 4" stroke="#fff" stroke-width="1.5" fill="none"/></svg></div>
  <div class="t-card light"><span class="q">&ldquo;</span>Lorem ipsum dolor sit amet, consectetur adipiscing elit. Nullam posuere felis vel ultricies, tum tellus ultrices sed nibh. Pellentesque vel est dui.</div>
  <div class="t-card dark"><span class="q">&ldquo;</span>Lorem ipsum dolor sit amet, consectetur adipiscing elit. Nullam posuere felis vel ultricies, tum tellus ultrices sed nibh. Pellentesque vel est dui.</div>
  <div class="t-person" style="left:252px"><span class="avatar" role="img" aria-label="Client photo"></span><div><b>Daniel Rourke</b><span class="stars">★★★★★</span></div></div>
  <div class="t-person" style="left:618px"><span class="avatar" role="img" aria-label="Client photo"></span><div><b>Helena Marsh</b><span class="stars">★★★★★</span></div></div>
</section>

<section class="section appointment" style="top:2472px;height:415px" role="img" aria-label="Soft seaside shoreline at sunrise">
  <div class="photo-ring" style="left:225px;top:45px;width:314px;height:314px">
    <div class="photo" role="img" aria-label="Man seated talking during a session" style="background:linear-gradient(160deg,#f1f1f0,#9a9b9d 55%,#3e4d5e)"></div>
  </div>
  <h2 class="heading script" style="left:550px;top:76px;font-size:38px">Make an Appointment</h2>
  <div class="field" style="left:550px;top:146px;width:439px">Name</div>
  <div class="field" style="left:550px;top:188px;width:230px">Email</div>
  <div class="field" style="left:785px;top:188px;width:204px">Phone</div>
  <div class="field" style="left:550px;top:231px;width:439px;height:72px;align-items:flex-start;padding-top:8px">Message</div>
  <div class="btn btn-teal" style="left:550px;top:320px;width:120px;height:30px">Submit Now</div>
</section>

<section class="section mailing" style="top:2887px;height:97px">
  <h2>Join Our Mailing List To Learn More:</h2>
  <div class="field" style="left:645px;top:30px;width:287px;height:38px">Enter Your Email Address...</div>
  <div class="abs" style="left:932px;top:30px;width:57px;height:38px;background:var(--teal);display:flex;align-items:center;justify-content:center"><svg width="18" height="18" viewBox="0 0 24 24"><path d="M2 12L22 3l-5 19-5-7z" fill="#fff"/></svg></div>
</section>

<footer class="section site-footer" style="top:2984px;height:348px">
  <div class="f-col" style="left:209px">
    <h4>Follow Us</h4><div class="rule"></div>
    <div class="f-brand"><span class="dot"></span>Brindle Oak<small>Wellness Aftercare</small></div>
    <div class="f-social"><span></span><span></span><span></span><span></span></div>
  </div>
  <div class="f-col" style="left:404px">
    <h4>Quick Links</h4><div class="rule"></div>
    <ul><li>Home</li><li>About Us</li><li>Services</li><li>PRESS</li><li>FAQ</li><li>Testimonials</li><li>Contact Us</li></ul>
  </div>
  <div class="f-col" style="left:564px;width:170px">
    <h4>Contact Details</h4><div class="rule"></div>
    <div class="contact-row"><svg width="12" height="14" viewBox="0 0 12 16"><path d="M6 0a6 6 0 0 0-6 6c0 4.5 6 10 6 10s6-5.5 6-10a6 6 0 0 0-6-6zm0 8.5A2.5 2.5 0 1 1 6 3.5a2.5 2.5 0 0 1 0 5z" fill="#25b4d3"/></svg><div><b>Location</b>123 Lorem ipsum dolor sit amet, suite - 9755</div></div>
    <div class="contact-row"><svg width="13" height="12" viewBox="0 0 16 12"><path d="M0 0h16v12H0z" fill="#25b4d3"/><path d="M0 0l8 7 8-7" stroke="#fff" fill="none"/></svg><div><b>Email us:</b>info@brindleoak.example</div></div>
    <div class="contact-row"><svg width="13" height="13" viewBox="0 0 24 24"><path fill="#25b4d3" d="M6.6 10.8a15 15 0 0 0 6.6 6.6l2.2-2.2c.3-.3.7-.4 1-.2 1.1.4 2.3.6 3.6.6.6 0 1 .4 1 1V20c0 .6-.4 1-1 1A17 17 0 0 1 3 4c0-.6.4-1 1-1h3.5c.6 0 1 .4 1 1 0 1.3.2 2.5.6 3.6.1.3 0 .7-.2 1z"/></svg><div><b>Call us at:</b>( 555 ) 014 - 2290</div></div>
  </div>
  <div class="photo-ring" style="left:724px;top:16px;width:314px;height:314px">
    <div class="photo" role="img" aria-label="Street map showing the clinic location" style="background:radial-gradient(circle at 45% 40%,#f2f0ea,#dfe4dc 60%,#cfd8cd)"></div>
  </div>
</footer>

<div class="copyright">© 2019 BRINDLEOAKWELLNESSAFTERCARE. ALL RIGHTS RESERVED</div>

</body>
</html>
```